7 values, 7 questions, 7 illustrations!

For a project to liven up corporate values we have designed 7 questions our employees should ask themselves at any time. To start marketing these, we want to have various outings (posters, cards, leaflets, etc) that illustrate these questions. preferably with a logo / font of its own. Look and feel / moodwords: construction, white / red / black, values, non negociable, fun, vintage, together.
The 7 questions are here (underlying value between brackets)
1. How can I broaden my knowledge about this? How can I share my knowledge? (knowledge)
2. How does this contribute to a good working atmosphere? (fun)
3. Have I understood this correctly? (listening)
4. What would the customer say? (client orientation)
5. How can I help, even beyond my job description? (teamwork)
6. Am I keeping my commitments to others, internal or externally? (reliability)
7. Have I said it all? (honesty)

Each question needs to get its own little illustration.
Attached an example of work I commissioned here 4 years ago. I like the look and feel of the drawings, but please do feel free to make your unique proposition. What I like is the simplicity of the drawings. I would like maybe illustrations that feel "hand drawn" - as they need to give a warm, authentic and "fun / happy / flowy" feeling to the campaign.
I also added the company logo so you have a feel of what colors to work with. I don't mind RED being the main color and the illustrations in white.
If things are not clear, or more information needed, please let me know.

Target Market(s)

Internal employees of the company

Industry/Entity Type

Construction Company

Requirements
Must have
• hand drawn look and feel, simple linings,

```html
<!DOCTYPE html>
<html lang="en">
<head>
<meta charset="utf-8">
<title>Knowledge – Values Poster</title>
<link rel="stylesheet" href="https://fonts.googleapis.com/css2?family=Anton&family=Barlow:wght@600;700&family=Outfit:wght@500;700&display=swap">
<style>
  :root {
    --red: #ec1c24;
    --white: #ffffff;
    --ink: #1d1d1b;
    --bulb-tone: #f15a5f;
  }
  html, body {
    margin: 0;
    padding: 0;
    width: 1200px;
    height: 1200px;
    overflow: hidden;
    background: var(--white);
  }
  .poster-canvas { display: block; width: 1200px; height: 1200px; }
  .poster-sheet { fill: var(--red); }
  .headline {
    font-family: "Anton", "Impact", sans-serif;
    font-size: 286px;
    fill: var(--red);
    stroke: var(--ink);
    stroke-width: 5;
    paint-order: stroke;
  }
  .ring-text { font-family: "Barlow", "Arial", sans-serif; fill: var(--white); font-weight: 700; }
  .ring-share { font-size: 44px; }
  .ring-increase { font-size: 38px; }
  .ring-critical { font-size: 31px; }
  .ring-small { font-size: 23px; font-weight: 600; }
  .side-panel { fill: var(--white); }
  .question {
    font-family: "Outfit", "Helvetica", sans-serif;
    font-weight: 500;
    font-size: 22px;
    fill: var(--ink);
  }
  .brand-name {
    font-family: "Outfit", "Helvetica", sans-serif;
    font-weight: 700;
    font-size: 27px;
    fill: var(--ink);
  }
  .brand-mark { fill: var(--red); }
  .bulb-illustration { fill: var(--bulb-tone); }
</style>
</head>
<body>
<svg class="poster-canvas" viewBox="0 0 1500 1500" xmlns="http://www.w3.org/2000/svg">
  <defs>
    <clipPath id="sheet-clip"><rect x="241" y="45" width="1006" height="1420"/></clipPath>
    <path id="ring-share" d="M -320 1110 A 650 650 0 1 1 980 1110 A 650 650 0 1 1 -320 1110"/>
    <path id="ring-increase" d="M -220 1110 A 550 550 0 1 1 880 1110 A 550 550 0 1 1 -220 1110"/>
    <path id="ring-critical" d="M -100 1110 A 430 430 0 1 1 760 1110 A 430 430 0 1 1 -100 1110"/>
    <path id="ring-small" d="M 10 1110 A 320 320 0 1 1 650 1110 A 320 320 0 1 1 10 1110"/>
  </defs>

  <rect class="poster-sheet" x="241" y="45" width="1006" height="1420"/>

  <g class="poster-content" clip-path="url(#sheet-clip)">
    <!-- headline -->
    <text class="headline" x="323" y="330" textLength="614" lengthAdjust="spacingAndGlyphs">KNOW</text>
    <text class="headline" transform="translate(965 125) rotate(90)" x="0" y="0" dy="0" textLength="580" lengthAdjust="spacingAndGlyphs"><tspan dy="-0">LEDGE</tspan></text>

    <!-- light bulb drawing area -->
    <rect class="bulb-illustration" x="265" y="885" width="290" height="400" rx="60" role="img" aria-label="Hand-drawn white line light bulb"/>

    <!-- circular text rings -->
    <g class="ring-text ring-share">
      <text><textPath href="#ring-share" startOffset="50" textLength="670" lengthAdjust="spacing">SHARE WHAT I KNOW</textPath></text>
      <text><textPath href="#ring-share" startOffset="970" textLength="670" lengthAdjust="spacing">SHARE WHAT I KNOW</textPath></text>
      <text><textPath href="#ring-share" startOffset="1890" textLength="670" lengthAdjust="spacing">SHARE WHAT I KNOW</textPath></text>
      <text><textPath href="#ring-share" startOffset="2810" textLength="670" lengthAdjust="spacing">SHARE WHAT I KNOW</textPath></text>
    </g>
    <g class="ring-text ring-increase">
      <text><textPath href="#ring-increase" startOffset="347" textLength="530" lengthAdjust="spacing">increase knowledge</textPath></text>
      <text><textPath href="#ring-increase" startOffset="1097" textLength="530" lengthAdjust="spacing">increase knowledge</textPath></text>
      <text><textPath href="#ring-increase" startOffset="1847" textLength="530" lengthAdjust="spacing">increase knowledge</textPath></text>
      <text><textPath href="#ring-increase" startOffset="2597" textLength="530" lengthAdjust="spacing">increase knowledge</textPath></text>
    </g>
    <g class="ring-text ring-critical">
      <text><textPath href="#ring-critical" startOffset="47" textLength="411" lengthAdjust="spacing">CRITICAL THINKING</textPath></text>
      <text><textPath href="#ring-critical" startOffset="623" textLength="411" lengthAdjust="spacing">CRITICAL THINKING</textPath></text>
      <text><textPath href="#ring-critical" startOffset="1199" textLength="411" lengthAdjust="spacing">CRITICAL THINKING</textPath></text>
      <text><textPath href="#ring-critical" startOffset="1775" textLength="411" lengthAdjust="spacing">CRITICAL THINKING</textPath></text>
    </g>
    <g class="ring-text ring-small">
      <text><textPath href="#ring-small" startOffset="101" textLength="245" lengthAdjust="spacing">capture the idea</textPath></text>
      <text><textPath href="#ring-small" startOffset="427" textLength="122" lengthAdjust="spacing">training</textPath></text>
      <text><textPath href="#ring-small" startOffset="668" textLength="245" lengthAdjust="spacing">capture the idea</textPath></text>
      <text><textPath href="#ring-small" startOffset="994" textLength="122" lengthAdjust="spacing">training</textPath></text>
      <text><textPath href="#ring-small" startOffset="1235" textLength="245" lengthAdjust="spacing">capture the idea</textPath></text>
      <text><textPath href="#ring-small" startOffset="1561" textLength="122" lengthAdjust="spacing">training</textPath></text>
    </g>

    <!-- question panel -->
    <rect class="side-panel" x="965" y="737" width="203" height="728"/>
    <text class="question" x="989" y="805">
      <tspan x="989">HOW CAN I</tspan>
      <tspan x="989" dy="28.5">BROADEN MY</tspan>
      <tspan x="989" dy="28.5">KNOWLEDGE</tspan>
      <tspan x="989" dy="28.5">ABOUT THIS?</tspan>
    </text>
    <text class="question" x="989" y="974">
      <tspan x="989">HOW CAN I</tspan>
      <tspan x="989" dy="28.5">SHARE MY</tspan>
      <tspan x="989" dy="28.5">KNOWLEDGE?</tspan>
    </text>

    <!-- brand -->
    <rect class="brand-mark" x="985" y="1385" width="22" height="22"/>
    <text class="brand-name" x="1017" y="1407">STRUCTA</text>
  </g>
</svg>
</body>
</html>
```